Supplement Company Needs a Protein Powder Pouch Design

We are looking for a modern and fresh design for our 500g pouches of protein powder as our current design is not eye catching or exciting enough.

This new design will be printed on both sides of a 178mm x 280mm x 101mm pouch.

We have 4 flavours. These are Banana Ice Cream, Chocolate Deluxe, Strawberries & Cream and Vanilla Ice Cream.
Updates

Need extra days to review

Industry/Entity Type

Supplement

Requirements
Must have
• Attractive and eye catching front and space for all the nutritional information and ingredients on the back.

Must clearly state 'food supplement' somewhere on the front of the pouch.
Nice to have
• Our logo is attached.
Should not have
• No health claims as these are not allowed in the UK

```html
<!DOCTYPE html>
<html lang="en">
<head>
<meta charset="utf-8">
<title>ZEST Supplements – Protein Powder Pouches</title>
<link href="https://fonts.googleapis.com/css2?family=Oswald:wght@500;600&family=Titillium+Web:wght@400;600;700&display=swap" rel="stylesheet">
<style>
:root{
  --pouch:#0d0d0d;
  --gold:#c9a86a;
  --gold-light:#e3c98f;
  --white:#ffffff;
  --cream:#e9dcae;
  --banana-text:#6b4a2a;
  --choc:#6e412a;
  --choc-light:#8a5a3c;
  --page:#ffffff;
  --rule:#444444;
}
*{margin:0;padding:0;box-sizing:border-box}
html,body{width:1200px;height:1000px;overflow:hidden;background:var(--page)}
.canvas{position:relative;width:1200px;height:1000px}

.pouch{position:absolute;top:298px;width:346px;height:522px;background:var(--pouch);border-radius:6px;overflow:hidden;font-family:"Titillium Web",sans-serif;color:var(--white)}
.pouch--back{left:62px;height:508px}
.pouch--banana{left:445px}
.pouch--chocolate{left:815px}

.brand{text-align:center;font-family:"Oswald",sans-serif;font-weight:600;color:var(--gold);letter-spacing:1px;line-height:1}

/* Back panel: flowing column so nothing overlaps */
.back-column{position:absolute;left:42px;right:6px;top:92px;display:flex;flex-direction:column}
.back-column .brand{font-size:21px;margin-bottom:20px}
.back-copy{font-size:11.5px;line-height:1.15;margin-bottom:6px}
.back-copy b{font-weight:700}
.nutrition{display:flex;gap:5px;font-size:6.4px;line-height:1.15;margin:2px 0 7px}
.nutrition .intro{width:78px;flex:none}
.nutrition .intro .cal{display:block;text-align:center;font-size:14px;font-weight:700;margin:1px 0}
.nutrition table{border-collapse:collapse;flex:1}
.nutrition td{padding:0 2px;border-bottom:1px solid var(--rule);white-space:nowrap}
.nutrition td:last-child{text-align:right}
.nutrition .sub{font-style:italic;padding-left:6px}
.small-print{font-size:6.2px;line-height:1.35;color:var(--gold);margin-bottom:5px}
.small-print--center{text-align:center;margin-bottom:4px}

/* Front panels */
.band{position:absolute;left:0;top:0;width:346px;height:522px}
.front .brand{position:absolute;left:0;right:0;top:118px;font-size:30px;color:var(--gold-light)}
.rule-label{position:absolute;left:45px;right:45px;top:192px;height:34px;border-top:2px solid var(--gold);border-bottom:2px solid var(--gold);text-align:center;font-family:"Oswald",sans-serif;font-weight:500;font-size:21px;line-height:30px;color:var(--gold);letter-spacing:.5px}
.title{position:absolute;left:0;right:0;text-align:center;font-family:"Oswald",sans-serif;font-weight:600;font-size:35px;line-height:1}
.title--protein{top:238px;color:var(--white)}
.title--powder{top:276px;color:var(--gold)}
.photo{position:absolute}
.photo--banana{left:95px;top:320px;width:156px;height:100px;border-radius:50%;background:radial-gradient(circle at 50% 40%,#f3e3b8,#d8b45a)}
.photo--chocolate{left:110px;top:326px;width:126px;height:84px;border-radius:6px;background:linear-gradient(135deg,#7b4a30,#3e2215)}
.flavour{position:absolute;left:0;right:0;top:432px;text-align:center;font-family:"Oswald",sans-serif;font-weight:600;font-size:23px;line-height:1.2}
.flavour--banana{color:var(--banana-text)}
.flavour--chocolate{color:var(--white)}
.weight{position:absolute;left:72px;right:72px;top:474px;height:26px;border-radius:13px;background:var(--gold);text-align:center;font-weight:700;font-size:14px;line-height:26px;color:var(--white)}
</style>
</head>
<body>
<div class="canvas">

  <section class="pouch pouch--back">
    <div class="back-column">
      <div class="brand">ZEST SUPPLEMENTS</div>
      <p class="back-copy"><b>SUGGESTED USE:</b> We recommend using one to two servings of 30g per day. One serving is one level scoop (a scoop is inside this pouch). Mix one level scoop with at least 200ml of cold water. Do not exceed recommended daily dose.</p>
      <p class="back-copy"><b>STORAGE INFORMATION:</b> Store in a cool and dry place. Reseal this pouch after each use. Keep out of sight and reach of children.</p>
      <div class="nutrition">
        <div class="intro"><b>Nutrition Information</b><br>Chocolate flavour protein food supplement with sweetener<br>Calories per 30g serving:<span class="cal">117</span>16 servings</div>
        <table>
          <tr><td><b>Typical values per 30g</b></td><td></td></tr>
          <tr><td>Energy</td><td>489kj</td></tr>
          <tr><td></td><td>117kcals</td></tr>
          <tr><td>Fat</td><td>1.8g</td></tr>
          <tr><td class="sub">of which saturates</td><td>0.08g</td></tr>
          <tr><td>Carbohydrate</td><td>4.2g</td></tr>
          <tr><td class="sub">of which sugars</td><td>3g</td></tr>
          <tr><td>Protein</td><td>21g</td></tr>
          <tr><td>Salt</td><td>0.2g</td></tr>
        </table>
        <table>
          <tr><td><b>Typical values per 100g</b></td><td></td></tr>
          <tr><td>Energy</td><td>1630kj</td></tr>
          <tr><td></td><td>390kcals</td></tr>
          <tr><td>Fat</td><td>6g</td></tr>
          <tr><td class="sub">of which saturates</td><td>0.1g</td></tr>
          <tr><td>Carbohydrate</td><td>14g</td></tr>
          <tr><td class="sub">of which sugars</td><td>10g</td></tr>
          <tr><td>Protein</td><td>70g</td></tr>
          <tr><td>Salt</td><td>0.8g</td></tr>
        </table>
      </div>
      <p class="small-print"><b>INGREDIENTS:</b> Protein Blend (<b>Soya</b> Protein Isolate, Whey Protein Concentrate (<b>Milk</b>), <b>Milk</b> Protein) (70%), Acetyl L-Carnitine (500mg per 100g), Acai Berry 4:1 Extract (400mg per 100g), Green Tea Extract (400mg per 100g), Conjugated Linoleic Acid Powder (500mg per 100g), Flavouring, Fat Reduced Cocoa Powder (10%), Thickener (Xanthan Gum), Sweetener (Sucralose).</p>
      <p class="small-print"><b>ALLERGEN INFORMATION:</b> For allergens, see ingredients in bold. May also contain cereal containing gluten, nuts, egg, peanuts.</p>
      <p class="small-print">CAUTION: Food supplements should not be used as a substitute for a varied diet and healthy lifestyle. This product is not recommended for use by pregnant or lactating women. If you are taking any medications or are under medical supervision, you should consult with your health care professional before use, taking into consideration other supplements and medications you consume. This product is not intended for use by persons under the age of 18.</p>
      <p class="small-print small-print--center">Manufactured in the UK with EU protein powder (Germany) and non-EU cocoa powder (Ghana).</p>
      <p class="small-print small-print--center">ZEST Supplements Limited, Mill Lane, Ashcombe, Devon, EX12 9QT.</p>
      <p class="small-print small-print--center">Best before: See back of pouch.</p>
    </div>
  </section>

  <section class="pouch pouch--banana front">
    <svg class="band" viewBox="0 0 346 522" aria-hidden="true">
      <path d="M0 330 Q173 365 346 330 L346 522 L0 522 Z" fill="var(--gold)"/>
      <path d="M14 345 Q173 378 332 345 L332 522 L14 522 Z" fill="var(--cream)"/>
    </svg>
    <div class="brand">ZEST SUPPLEMENTS</div>
    <div class="rule-label">FOOD SUPPLEMENT</div>
    <div class="title title--protein">PROTEIN</div>
    <div class="title title--powder">POWDER</div>
    <div class="photo photo--banana" role="img" aria-label="Scoop of banana ice cream with banana slices"></div>
    <div class="flavour flavour--banana">BANANA ICE CREAM</div>
    <div class="weight">500g NET WEIGHT</div>
  </section>

  <section class="pouch pouch--chocolate front">
    <svg class="band" viewBox="0 0 346 522" aria-hidden="true">
      <path d="M0 330 Q173 365 346 330 L346 522 L0 522 Z" fill="var(--choc-light)"/>
      <path d="M14 345 Q173 378 332 345 L332 522 L14 522 Z" fill="var(--choc)"/>
    </svg>
    <div class="brand">ZEST SUPPLEMENTS</div>
    <div class="rule-label">FOOD SUPPLEMENT</div>
    <div class="title title--protein">PROTEIN</div>
    <div class="title title--powder">POWDER</div>
    <div class="photo photo--chocolate" role="img" aria-label="Stacked pieces of milk chocolate bar"></div>
    <div class="flavour flavour--chocolate">CHOCOLATE DELUXE</div>
    <div class="weight">500g NET WEIGHT</div>
  </section>

</div>
</body>
</html>
```